"The Craft of Patron Care," fourth edition cover design

Later this year, my publisher, Harold Penmarsh & Daughters, will issue a fourth, substantially revised edition of "The Craft of Patron Care," following the 2016 publication of the third edition and the second and first versions that were issued earlier.

To distinguish this new edition from previous ones, I need a cover design that visually connects and is consistent with what has preceded it, while signaling this is a new and different, worthy of prospective readers/buyers’ attention.

Attached are three different verbal approaches to the new cover; these are NOT MEANT to serve as actual designs, but rather will give you a sense of how language is to be deployed:

The first emphasizes “ART” as the key visual word in the book title;
The second emphasizes “CLIENT SERVICE” as the key visual words in the book title; and,
The third emphasizes just the word "CLIENT" in the book title.

A top-of-the-page is a pre-head that applies to all three versions:
“6 TIMELESS PRINCIPLES FOR ADVERTISING & MARKETING PRO’s
IN AN AI WORLD"

There's a mid-page sub-head for all three versions:
“THE CLASSIC GUIDE,” followed by
“FOURTH EDITION BY GERALD ASHCOMBE

And there's a one-line, bottom-of-the-page designation:
“Foreword by Mae Dunford, Global Executive Creative Director, Starbolt"

The pallette for the previously published third edition was black with red as an accent color on a field of white; I've attached a sample for reference, so you can see how it was executed. For this new fourth edition, I'd like to change the accent color from red to either Wedgewood blue, or British racing green, or an alternative that is assertive and color saturated -- think of primary colors -- that contrast sufficiently with the base of black. As an alternative, you can consider a cover that used either Wedgewood blue, British racing green, or another possibility as a full-bleed field, with copy content either revered out or surprinted.

Lastly, while the new cover largely is meant to be typographically driven, if you can come up with a visual metaphor that illustrates and builds on the book's title, that would be very helpful. By way of reference, the third edition's book cover attempted to do this by introducing a visual element at the end of the book's title that's meant to represent an artist's paint splatter (although I admit it didn't work as well as it should).

Target Market(s)

Prospective purchasers of the book who might discover copies at a bookstore, but more likely will encounter it through online distributors such as Riverdex, Hartwell & Pike, and Tindall’s.

Industry/Entity Type

Advertising and marketing

Font styles to use
Serif
Sans Serif
Other font styles liked:
• A mix of serif and san-serif typefaces is okay. for the examples I shared, I relieid on "Arial Rounded Bold" but you need not be weeded to this. If you opt to mix in a serif font, I am partial to Cambria as a typeface.

Requirements
Must have
• To achieve the goal of being “connected with but distinct” from previous editions, the new cover should be:  Largely typographic, but displaying a color palette different from the previous editions’ black-plus-red-accent on a canvas of white.  Any new accent color selected for use should be vibrant, strong, and highly saturated; think “British racing green,” “Wedgewood blue,” or their equivalents.  In addition to a powerful, “billboard” approach to type and color, consider other visual metaphors that are likely to engage the readers. The winning cover design will stand out from other books, while connecting with the previously published third edition.
Nice to have
• If you can find way to illustrate the book's title through a visual metaphor, that would be ideal.a
Should not have
• Anything that is frivolous or non-sensical

```html
<!DOCTYPE html>
<html lang="en">
<head>
<meta charset="utf-8">
<title>The Craft of Patron Care — Fourth Edition Cover</title>
<link href="https://fonts.googleapis.com/css2?family=Poppins:wght@400;600;700;800&display=swap" rel="stylesheet">
<style>
  :root {
    --page: #ffffff;
    --ink: #000000;
    --title-ink: #231f20;
    --accent: #1a56b0;
    --frame: #231f20;
  }
  html, body {
    margin: 0;
    padding: 0;
    width: 1200px;
    height: 1200px;
    overflow: hidden;
    background: var(--page);
  }
  .cover {
    display: block;
    width: 1200px;
    height: 1200px;
    font-family: "Poppins", Arial, sans-serif;
  }
  .cover-frame { fill: var(--page); stroke: var(--frame); stroke-width: 2; }
  .prehead { font-weight: 700; font-size: 38px; fill: var(--ink); }
  .title-accent { font-weight: 800; font-size: 380px; fill: var(--accent); }
  .title-small { font-weight: 800; font-size: 70px; fill: var(--ink); }
  .title-line-one { font-weight: 800; font-size: 276px; fill: var(--title-ink); }
  .title-line-two { font-weight: 800; font-size: 228px; fill: var(--title-ink); }
  .subhead { font-weight: 700; font-size: 68px; fill: var(--ink); }
  .author { font-weight: 600; font-size: 56px; fill: var(--ink); }
  .foreword { font-weight: 400; font-size: 30px; fill: var(--ink); }
</style>
</head>
<body>
<svg class="cover" viewBox="0 0 1932 1932" xmlns="http://www.w3.org/2000/svg" role="img" aria-label="The Craft of Patron Care, fourth edition, by Gerald Ashcombe">
  <rect class="cover-frame" x="439" y="180" width="1070" height="1605"/>

  <g class="prehead-group" text-anchor="middle">
    <text class="prehead" x="973" y="352">6 TIMELESS PRINCIPLES FOR ADVERTISING &amp;</text>
    <text class="prehead" x="978" y="398">MARKETING PRO’s IN AN AI WORLD</text>
  </g>

  <g class="title-block">
    <text class="title-small" transform="translate(593 812) rotate(-90)">THE</text>
    <text class="title-accent" x="612" y="812" textLength="712" lengthAdjust="spacingAndGlyphs">CRAFT</text>
    <text class="title-small" transform="translate(1338 700) rotate(90)">OF</text>
    <text class="title-line-one" x="545" y="1030" textLength="860" lengthAdjust="spacingAndGlyphs">PATRON</text>
    <text class="title-line-two" x="545" y="1218" textLength="848" lengthAdjust="spacing">CARE</text>
  </g>

  <g class="subhead-group" text-anchor="middle">
    <text class="subhead" x="978" y="1390">THE CLASSIC GUIDE</text>
    <text class="subhead" x="978" y="1466">FOURTH EDITION</text>
  </g>

  <g class="credits" text-anchor="middle">
    <text class="author" x="985" y="1655">GERALD ASHCOMBE</text>
    <text class="foreword" x="978" y="1693">FOREWORD BY MAE DUNFORD, GLOBAL EXECUTIVE</text>
    <text class="foreword" x="978" y="1728">CREATIVE DIRECTOR, STARBOLT</text>
  </g>
</svg>
</body>
</html>
```